Locksmith Security Services Flyer

I'm looking for a flyer to high light services I offer within the locksmith industry. I don't require all services on the flyer. but it would be nice if they can be put on there. Logo needs to be on there as well as contact number , website and email address, and if possible other pictures, I would like it bright but it needs to be professional and have the "Stalwart" Look

Target Market(s)

Property owners

Industry/Entity Type

Locksmith

Font styles to use
Serif
Sans Serif

Requirements
Must have
• Contact number : 0800 562 7093
Website : www.stalwartalliance.co.uk
Email : locksmith@stalwartalliance.co.uk
Nice to have
• Lock Changes
Lock Upgrades
Lock Outs
Master key system
Keyed Alike
Key Cutting
Board ups

```html
<!DOCTYPE html>
<html lang="en">
<head>
<meta charset="utf-8">
<title>Stalwart Locksmith Services Flyer</title>
<link href="https://fonts.googleapis.com/css2?family=Oswald:wght@300;400;500;600&family=Open+Sans:wght@400;600&display=swap" rel="stylesheet">
<style>
:root{
  --blue:#3d3ba3;
  --navy:#2b2878;
  --ink:#222228;
  --grey:#efeff3;
  --footer:#16161a;
  --bg:#d9d9dc;
  --white:#ffffff;
}
*{margin:0;padding:0;box-sizing:border-box}
html,body{width:717px;height:1200px;overflow:hidden;background:var(--bg)}
body{position:relative;font-family:"Open Sans",Arial,sans-serif;color:var(--ink)}
.page{position:absolute;left:154px;width:408px;height:576px;background:var(--white);overflow:hidden;box-shadow:0 4px 14px rgba(0,0,0,.25)}
.page--front{top:16px}
.page--back{top:608px}
.abs{position:absolute}
.heading{font-family:"Oswald",Arial,sans-serif;font-weight:500;color:var(--ink);font-size:13px;line-height:1;display:flex;align-items:center;gap:5px;text-transform:uppercase;letter-spacing:.2px}
.tick{width:9px;height:9px;flex:none}
.copy{font-size:6.6px;line-height:1.38;text-align:justify;color:#333}
.price{position:absolute;height:18px;background:var(--blue);color:var(--white);border-radius:4px;font-family:"Oswald",Arial,sans-serif;font-weight:500;font-size:5.4px;letter-spacing:.1px;text-transform:uppercase;display:flex;align-items:center;justify-content:center;text-align:center;line-height:1.2;box-shadow:0 4px 5px rgba(40,38,120,.25)}
.footer{position:absolute;left:0;bottom:0;width:100%;height:28px;background:var(--footer);color:var(--white);display:flex;align-items:center;justify-content:space-around;padding:0 10px;font-family:"Oswald",Arial,sans-serif;font-weight:300;font-size:8.6px}
.footer span{display:flex;align-items:center;gap:4px}
.footer svg{width:7px;height:7px}
.ribbon{position:absolute;background:var(--navy);color:var(--white);font-family:"Oswald",Arial,sans-serif;font-weight:500;text-transform:uppercase;display:flex;align-items:center;justify-content:center}
/* front */
.hero-photo{left:0;top:0;width:408px;height:250px;background:linear-gradient(120deg,#c9c3bd 0%,#a88f7d 35%,#d7d4d2 60%,#8d8f96 100%)}
.hero-shapes{left:0;top:0;width:408px;height:340px}
.brand{left:22px;top:70px;width:126px;display:flex;flex-direction:column;align-items:center;gap:6px;color:var(--white);font-family:"Oswald",Arial,sans-serif;font-weight:500;font-size:14px;text-transform:uppercase;text-align:center;line-height:1.1}
.brand-mark{width:30px;height:30px;border:2px solid var(--white);border-radius:50%}
.circle-photo{left:218px;top:166px;width:168px;height:168px;border-radius:50%;border:5px solid var(--blue);background:radial-gradient(circle at 45% 40%,#c89c84 0%,#7b6f73 45%,#4c5160 100%)}
.greeting{left:22px;top:229px;font-family:"Oswald",Arial,sans-serif;font-weight:600;font-size:27px;color:var(--blue);line-height:1}
.greeting-copy{left:22px;top:262px;width:176px;font-size:6.8px;line-height:1.45;color:#333}
/* back */
.services-box{left:24px;top:261px;width:360px;height:113px;border:1.4px solid var(--blue);border-radius:6px}
.mobile-title{left:24px;top:281px;width:360px;text-align:center;font-weight:600;font-size:10px}
.mobile-copy{left:24px;top:296px;width:360px;text-align:center;font-size:8px;line-height:1.35;color:#333}
.responses{left:34px;top:334px;width:340px;height:28px;display:flex;justify-content:space-between}
.response{display:flex;align-items:center;gap:6px;font-size:10px;line-height:1.1;color:#222;flex:1;padding-left:4px}
.response+.response{border-left:1px dashed var(--blue)}
.response svg{width:20px;height:20px;flex:none}
.lock-photo{left:40px;top:380px;width:330px;height:160px;background:radial-gradient(ellipse at 50% 50%,#b8b0a0 0%,#cfd0d3 35%,#ffffff 72%)}
</style>
</head>
<body>

<section class="page page--front">
  <div class="abs hero-photo" role="img" aria-label="Locksmith fitting a lock to a glass door with a screwdriver"></div>
  <svg class="abs hero-shapes" viewBox="0 0 408 340" aria-hidden="true">
    <polygon points="0,0 60,0 0,50" fill="#efeff3"/>
    <polygon points="0,50 60,0 250,176 236,184 0,229" fill="#3d3ba3"/>
    <polygon points="0,229 236,184 408,160 408,310 0,322" fill="#efeff3"/>
    <polygon points="330,200 408,150 408,170 345,205" fill="#3d3ba3"/>
    <polygon points="0,322 408,310 408,340 0,340" fill="#ffffff"/>
  </svg>
  <div class="abs brand"><span class="brand-mark"></span>Stalwart<br>Locksmiths</div>
  <div class="abs circle-photo" role="img" aria-label="Key cutter at work in a workshop"></div>

  <h1 class="abs greeting">GREETING</h1>
  <p class="abs greeting-copy">Thank you for taking my call today, Stalwart Partnership offer all services a client may require within the Security and Locksmith industry as requested please find below more information on how we can help and support you.</p>

  <div class="ribbon" style="left:24px;top:326px;width:172px;height:25px;font-size:13px;clip-path:polygon(0 0,100% 0,93% 50%,100% 100%,0 100%)">Locksmith Services</div>

  <div class="abs" style="left:24px;top:365px;width:172px">
    <h2 class="heading"><svg class="tick" viewBox="0 0 10 10"><circle cx="5" cy="5" r="4.2" fill="none" stroke="#3d3ba3" stroke-width="1"/><path d="M3 5.2l1.5 1.5L7.3 3.6" fill="none" stroke="#3d3ba3" stroke-width="1.1"/></svg>Lock Outs</h2>
    <p class="copy" style="margin-top:5px">This service is offered 24 hours a day, 7 days a week, we are happy for your tenants to contact us directly.</p>
  </div>
  <div class="price" style="left:24px;top:421px;width:172px">Prices start at £65 depending on time day.</div>

  <div class="abs" style="left:24px;top:455px;width:172px">
    <h2 class="heading"><svg class="tick" viewBox="0 0 10 10"><circle cx="5" cy="5" r="4.2" fill="none" stroke="#3d3ba3" stroke-width="1"/><path d="M3 5.2l1.5 1.5L7.3 3.6" fill="none" stroke="#3d3ba3" stroke-width="1.1"/></svg>Lock Changes</h2>
    <p class="copy" style="margin-top:5px">This service means we can change the locks in a property. We offer different packages for this dependent on what level of security lock we are changing for.</p>
  </div>
  <div class="price" style="left:24px;top:515px;width:172px;height:20px">Prices start at £49<br>(assuming entry does not need to be gained)</div>

  <div class="abs" style="left:218px;top:348px;width:165px">
    <h2 class="heading"><svg class="tick" viewBox="0 0 10 10"><circle cx="5" cy="5" r="4.2" fill="none" stroke="#3d3ba3" stroke-width="1"/><path d="M3 5.2l1.5 1.5L7.3 3.6" fill="none" stroke="#3d3ba3" stroke-width="1.1"/></svg>Lock/Security Upgrades</h2>
    <p class="copy" style="margin-top:5px">With strategic partnerships with many lock suppliers we can offer lock upgrades including 3* and Sapphire Guard as well as adding extra locks and security devices to properties.</p>
  </div>
  <div class="price" style="left:218px;top:410px;width:165px">Prices quoted dependent on customer requirements.</div>

  <div class="abs" style="left:218px;top:446px;width:165px">
    <h2 class="heading"><svg class="tick" viewBox="0 0 10 10"><circle cx="5" cy="5" r="4.2" fill="none" stroke="#3d3ba3" stroke-width="1"/><path d="M3 5.2l1.5 1.5L7.3 3.6" fill="none" stroke="#3d3ba3" stroke-width="1.1"/></svg>Board Ups</h2>
    <p class="copy" style="margin-top:5px">Our vehicles carry all the equipment required for board up as well as a full stocked unit meaning we are available 24 hours a days 7 days a week should a customer require a property making safe after burglary or smashed window.</p>
  </div>
  <div class="price" style="left:218px;top:517px;width:165px">Prices start at £70</div>

  <footer class="footer">
    <span><svg viewBox="0 0 10 10"><path d="M2 1l2 2-1 1.5c.8 1.5 1.8 2.5 3.3 3.3L7.8 6.8l2 2-1.5 1.2C4.5 9.5.5 5.5 0 1.7z" fill="#fff"/></svg>0800 562 7093</span>
    <span><svg viewBox="0 0 10 10"><circle cx="5" cy="5" r="4.3" fill="none" stroke="#fff"/><path d="M.7 5h8.6M5 .7c-2.5 2.5-2.5 6.1 0 8.6M5 .7c2.5 2.5 2.5 6.1 0 8.6" fill="none" stroke="#fff" stroke-width=".8"/></svg>www.stalwartalliance.co.uk</span>
    <span><svg viewBox="0 0 10 10"><rect x=".5" y="2" width="9" height="6.5" fill="#fff"/><path d="M.5 2L5 5.7 9.5 2" fill="none" stroke="#16161a" stroke-width=".8"/></svg>locksmith@stalwartalliance.co.uk</span>
  </footer>
</section>

<section class="page page--back">
  <div class="abs" style="left:24px;top:22px;width:173px">
    <h2 class="heading"><svg class="tick" viewBox="0 0 10 10"><circle cx="5" cy="5" r="4.2" fill="none" stroke="#3d3ba3" stroke-width="1"/><path d="M3 5.2l1.5 1.5L7.3 3.6" fill="none" stroke="#3d3ba3" stroke-width="1.1"/></svg>Key Cutting</h2>
    <p class="copy" style="margin-top:5px">We can cut all residential and commercial keys using top of the range equipment and full stocked blacks we are able to not only cut keys for existing locks but also provide extra for newly installed locks.</p>
  </div>
  <div class="price" style="left:24px;top:91px;width:173px">Prices dependent on customer requirement.</div>

  <div class="abs" style="left:24px;top:129px;width:173px">
    <h2 class="heading"><svg class="tick" viewBox="0 0 10 10"><circle cx="5" cy="5" r="4.2" fill="none" stroke="#3d3ba3" stroke-width="1"/><path d="M3 5.2l1.5 1.5L7.3 3.6" fill="none" stroke="#3d3ba3" stroke-width="1.1"/></svg>Master Key Systems</h2>
    <p class="copy" style="margin-top:5px;text-align:left">Master key systems are a way for one key to open all locks on a system while still having keys that are only able to open on individual locks, perfect for office blocks where the caretaker has access to all rooms, but each tenant only has access to their own.</p>
  </div>
  <div class="price" style="left:24px;top:207px;width:173px">Prices quoted dependent on customer requirement.</div>

  <div class="abs" style="left:220px;top:22px;width:167px">
    <h2 class="heading"><svg class="tick" viewBox="0 0 10 10"><circle cx="5" cy="5" r="4.2" fill="none" stroke="#3d3ba3" stroke-width="1"/><path d="M3 5.2l1.5 1.5L7.3 3.6" fill="none" stroke="#3d3ba3" stroke-width="1.1"/></svg>Keyed Alike</h2>
    <p class="copy" style="margin-top:5px">Keyed alike gives customers the option to have one key for all locks on a property. E.g., Front door, Back door, Garage, and padlock on out building are all operated using the same key.</p>
  </div>
  <div class="price" style="left:220px;top:83px;width:167px">Prices quoted dependent on customer requirement.</div>

  <div class="abs" style="left:220px;top:122px;width:167px">
    <h2 class="heading"><svg class="tick" viewBox="0 0 10 10"><circle cx="5" cy="5" r="4.2" fill="none" stroke="#3d3ba3" stroke-width="1"/><path d="M3 5.2l1.5 1.5L7.3 3.6" fill="none" stroke="#3d3ba3" stroke-width="1.1"/></svg>Key Holding</h2>
    <p class="copy" style="margin-top:5px">Mainly used as part of our security services our key holding service means we store your property keys. This reduces the cost of having locks changed if a key is lost as we can use one of our response vehicles to deliver these to you. Can also be incorporated with our lock up and unlock service and Alarm response.</p>
  </div>
  <div class="price" style="left:220px;top:209px;width:167px">Key holding costs start at less than £1 per day.</div>

  <div class="abs services-box"></div>
  <div class="ribbon" style="left:128px;top:249px;width:152px;height:24px;font-size:13px;clip-path:polygon(0 0,100% 0,94% 100%,6% 100%)">Security Services</div>
  <h3 class="abs mobile-title">MOBILE RESPONSE</h3>
  <p class="abs mobile-copy">Stalwart Partnership use our marked vehicles to attend<br>properties for multiple reasons.</p>
  <div class="abs responses">
    <div class="response"><svg viewBox="0 0 20 20"><circle cx="10" cy="10" r="9.3" fill="#3d3ba3"/><circle cx="10" cy="10" r="7.6" fill="none" stroke="#fff" stroke-width=".7"/><path d="M7 13V9.5a3 3 0 016 0V13zM6 13.5h8v1.2H6z" fill="#fff"/></svg>Alarm<br>Response</div>
    <div class="response"><svg viewBox="0 0 20 20"><circle cx="10" cy="10" r="9.3" fill="#3d3ba3"/><circle cx="10" cy="10" r="7.6" fill="none" stroke="#fff" stroke-width=".7"/><rect x="6.5" y="9" width="7" height="5.5" fill="#fff"/><path d="M8 9V7.5a2 2 0 014 0V9" fill="none" stroke="#fff" stroke-width="1"/></svg>Lock up /<br>Unlocks</div>
    <div class="response"><svg viewBox="0 0 20 20"><circle cx="10" cy="10" r="9.3" fill="#3d3ba3"/><circle cx="10" cy="10" r="7.6" fill="none" stroke="#fff" stroke-width=".7"/><path d="M10 5l4 1.5v3c0 2.6-1.8 4.4-4 5.3-2.2-.9-4-2.7-4-5.3v-3z" fill="none" stroke="#fff" stroke-width="1"/><path d="M8.3 10l1.2 1.2 2.2-2.2" fill="none" stroke="#fff" stroke-width=".9"/></svg>Security<br>Checks</div>
  </div>

  <div class="abs lock-photo" role="img" aria-label="Chrome door knob lock set with miniature worker figures"></div>

  <footer class="footer">
    <span><svg viewBox="0 0 10 10"><path d="M2 1l2 2-1 1.5c.8 1.5 1.8 2.5 3.3 3.3L7.8 6.8l2 2-1.5 1.2C4.5 9.5.5 5.5 0 1.7z" fill="#fff"/></svg>0800 562 7093</span>
    <span><svg viewBox="0 0 10 10"><circle cx="5" cy="5" r="4.3" fill="none" stroke="#fff"/><path d="M.7 5h8.6M5 .7c-2.5 2.5-2.5 6.1 0 8.6M5 .7c2.5 2.5 2.5 6.1 0 8.6" fill="none" stroke="#fff" stroke-width=".8"/></svg>www.stalwartalliance.co.uk</span>
    <span><svg viewBox="0 0 10 10"><rect x=".5" y="2" width="9" height="6.5" fill="#fff"/><path d="M.5 2L5 5.7 9.5 2" fill="none" stroke="#16161a" stroke-width=".8"/></svg>locksmith@stalwartalliance.co.uk</span>
  </footer>
</section>

</body>
</html>
```